Kitchen Cabinet Company Van Wrap / Partial Wrap with Spot Graphics

We would like our Halvik Stride High Roof Cargo van wrapped with our logo and possibly some job photos from our Dwelbo / Friendora page. @verdellcabinets
Not necessary a full wrap but at least logo and graphics / business info.
Something clean and contemporary and not to busy.
Eyecatching and sleek.
https://www.friendora.example/VerdellCabinets
www.Dwelbo.example/pro/VerdellCabinets/verdell-cabinets-and-design

Target Market(s)

High End

Requirements
Must have
• Clear Logo and one Large Image per side.
Design needs to be easy to see and portray what we do from a distance.
Nice to have
• A partial wrap with spot graphics is preferred. For example, maybe a large kitchen image toward the rear (side) of the van with logo and information in front.
Should not have
• Not too busy.

```html
<!DOCTYPE html>
<html lang="en">
<head>
<meta charset="utf-8">
<title>Verdell Cabinets &amp; Design – Van Wrap</title>
<link rel="stylesheet" href="https://fonts.googleapis.com/css2?family=Cinzel:wght@500&family=Didact+Gothic&display=swap">
<style>
  :root {
    --maroon: #6e1b1d;
    --maroon-deep: #4a1416;
    --body-white: #f6f6f4;
    --trim-grey: #44464a;
    --tyre: #1c1c1e;
    --glass: #2a2d31;
    --ink: #2b2b2b;
    --soft-grey: #7b7b7b;
    --stage: #ececec;
    --photo-light: #e6e0d6;
    --photo-mid: #c7b9a6;
    --photo-floor: #a4835e;
  }
  html, body { margin: 0; padding: 0; }
  body {
    width: 1200px; height: 3075px; overflow: hidden;
    background: var(--stage);
  }
  .wrap-view { display: block; width: 1200px; }
  .side-driver { height: 561px; }
  .side-passenger { height: 603px; }
  .front-view { height: 890px; }
  .rear-view { height: 1021px; }
  .brand-name { font-family: "Cinzel", serif; font-weight: 500; }
  .sans { font-family: "Didact Gothic", sans-serif; }
  .body-panel { fill: var(--body-white); stroke: #cfcfcf; stroke-width: 2; }
  .trim { fill: var(--trim-grey); }
  .tyre { fill: var(--tyre); }
  .glass { fill: var(--glass); }
  .accent { fill: var(--maroon); }
</style>
</head>
<body>

<!-- Driver side -->
<svg class="wrap-view side-driver" viewBox="0 0 1200 561" xmlns="http://www.w3.org/2000/svg">
  <defs>
    <linearGradient id="kitchenA" x1="0" y1="0" x2="0" y2="1">
      <stop offset="0" stop-color="var(--photo-light)"/>
      <stop offset="0.65" stop-color="var(--photo-mid)"/>
      <stop offset="1" stop-color="var(--photo-floor)"/>
    </linearGradient>
  </defs>
  <path class="body-panel" d="M60,330 L75,280 Q140,200 215,160 L250,60 Q275,30 330,28 L1060,28 Q1108,32 1112,80 L1122,420 L1118,465 L60,465 Z"/>
  <rect class="trim" x="48" y="382" width="1076" height="83" rx="10"/>
  <path class="glass" d="M232,170 L262,100 Q270,88 290,88 L410,88 L410,300 L180,300 Q200,220 232,170 Z"/>
  <rect x="665" y="28" width="455" height="352" fill="url(#kitchenA)" role="img" aria-label="Photo of a bright white kitchen with wood floor and dark lower cabinets"/>
  <polygon class="accent" points="662,28 700,28 815,380 770,380"/>
  <polygon points="700,28 740,28 830,380 815,380" fill="var(--body-white)" opacity="0.5"/>
  <rect x="278" y="433" width="540" height="22" fill="var(--maroon-deep)"/>
  <text class="sans" x="548" y="450" font-size="17" letter-spacing="3" fill="#fff" text-anchor="middle">www.verdellcabinets.example</text>
  <rect class="accent" x="553" y="158" width="34" height="34"/>
  <text class="brand-name" x="570" y="260" font-size="42" fill="var(--maroon)" text-anchor="middle" letter-spacing="2">VERDELL</text>
  <text class="sans" x="570" y="278" font-size="14" fill="var(--soft-grey)" text-anchor="middle" letter-spacing="3">CABINETS &amp; DESIGN</text>
  <text class="sans" x="570" y="325" font-size="27" fill="var(--ink)" text-anchor="middle" letter-spacing="2">(504) 555-0187</text>
  <text class="sans" x="570" y="345" font-size="15" fill="var(--soft-grey)" text-anchor="middle" letter-spacing="3">@verdellcabinets</text>
  <circle class="tyre" cx="190" cy="460" r="70"/>
  <circle class="tyre" cx="910" cy="465" r="70"/>
</svg>

<!-- Passenger side -->
<svg class="wrap-view side-passenger" viewBox="0 0 1200 603" xmlns="http://www.w3.org/2000/svg">
  <defs>
    <linearGradient id="kitchenB" x1="0" y1="0" x2="0" y2="1">
      <stop offset="0" stop-color="var(--photo-light)"/>
      <stop offset="0.6" stop-color="#cbc3b8"/>
      <stop offset="1" stop-color="var(--photo-floor)"/>
    </linearGradient>
  </defs>
  <path class="body-panel" d="M1140,380 L1125,330 Q1060,240 985,200 L950,95 Q925,65 870,64 L140,64 Q92,68 88,115 L78,450 L82,505 L1140,505 Z"/>
  <rect class="trim" x="76" y="418" width="1118" height="87" rx="10"/>
  <path class="glass" d="M968,205 L938,135 Q930,122 910,122 L790,122 L790,330 L1010,330 Q1000,255 968,205 Z"/>
  <rect x="80" y="64" width="440" height="354" fill="url(#kitchenB)" role="img" aria-label="Photo of a white kitchen with island, bar stools and pendant lights"/>
  <polygon class="accent" points="520,64 480,64 395,418 440,418"/>
  <rect class="glass" x="468" y="140" width="272" height="150" rx="14"/>
  <rect x="360" y="468" width="585" height="22" fill="var(--maroon-deep)"/>
  <text class="sans" x="655" y="485" font-size="17" letter-spacing="3" fill="#fff" text-anchor="middle">www.verdellcabinets.example</text>
  <rect class="accent" x="594" y="160" width="34" height="34"/>
  <text class="brand-name" x="611" y="252" font-size="40" fill="#e9e4e0" text-anchor="middle" letter-spacing="2">VERDELL</text>
  <text class="sans" x="611" y="270" font-size="14" fill="#cfcfcf" text-anchor="middle" letter-spacing="3">CABINETS &amp; DESIGN</text>
  <text class="sans" x="611" y="354" font-size="27" fill="var(--ink)" text-anchor="middle" letter-spacing="2">(504) 555-0187</text>
  <text class="sans" x="611" y="376" font-size="15" fill="var(--soft-grey)" text-anchor="middle" letter-spacing="3">@verdellcabinets</text>
  <circle class="tyre" cx="250" cy="500" r="72"/>
  <circle class="tyre" cx="1035" cy="495" r="72"/>
</svg>

<!-- Front -->
<svg class="wrap-view front-view" viewBox="0 0 1200 890" xmlns="http://www.w3.org/2000/svg">
  <path class="body-panel" d="M360,20 Q600,5 840,20 L885,180 L900,320 L945,420 L948,700 L252,700 L255,420 L300,320 L315,180 Z"/>
  <rect class="accent" x="583" y="30" width="34" height="34"/>
  <text class="brand-name" x="600" y="130" font-size="40" fill="var(--maroon)" text-anchor="middle" letter-spacing="2">VERDELL</text>
  <rect class="accent" x="495" y="138" width="210" height="20" rx="4"/>
  <text class="sans" x="600" y="153" font-size="14" fill="#fff" text-anchor="middle" letter-spacing="3">CABINETS &amp; DESIGN</text>
  <path class="glass" d="M330,185 Q600,170 870,185 L880,415 Q600,400 320,415 Z"/>
  <rect class="trim" x="205" y="335" width="70" height="110" rx="18"/>
  <rect class="trim" x="925" y="335" width="70" height="110" rx="18"/>
  <path d="M280,460 L390,440 L395,500 L285,520 Z" fill="#bfc3c7"/>
  <path d="M920,460 L810,440 L805,500 L915,520 Z" fill="#bfc3c7"/>
  <rect class="trim" x="405" y="470" width="390" height="130" rx="30"/>
  <g fill="#8a8d91">
    <rect x="430" y="495" width="340" height="8"/>
    <rect x="430" y="525" width="340" height="8"/>
    <rect x="430" y="555" width="340" height="8"/>
  </g>
  <path class="trim" d="M252,610 L948,610 L945,740 Q600,770 255,740 Z"/>
  <rect class="tyre" x="258" y="740" width="80" height="120" rx="12"/>
  <rect class="tyre" x="862" y="740" width="80" height="120" rx="12"/>
</svg>

<!-- Rear -->
<svg class="wrap-view rear-view" viewBox="0 0 1200 1021" xmlns="http://www.w3.org/2000/svg">
  <defs>
    <linearGradient id="kitchenC" x1="0" y1="0" x2="0" y2="1">
      <stop offset="0" stop-color="#efebe5"/>
      <stop offset="0.55" stop-color="#d9d2c8"/>
      <stop offset="0.78" stop-color="#c4ab8c"/>
      <stop offset="1" stop-color="var(--photo-floor)"/>
    </linearGradient>
  </defs>
  <path class="body-panel" d="M290,15 Q600,0 910,15 L965,490 L985,780 L215,780 L235,490 Z"/>
  <path d="M295,20 Q600,5 905,20 L960,490 L978,715 L222,715 L240,490 Z" fill="url(#kitchenC)" role="img" aria-label="Photo of a white kitchen with marble backsplash, island and gold bar stools"/>
  <rect x="535" y="8" width="130" height="16" rx="6" fill="var(--maroon)"/>
  <rect class="accent" x="560" y="85" width="80" height="80"/>
  <text class="brand-name" x="600" y="290" font-size="86" fill="var(--maroon)" text-anchor="middle" letter-spacing="4">VERDELL</text>
  <rect class="accent" x="385" y="310" width="445" height="38" rx="8"/>
  <text class="sans" x="607" y="338" font-size="28" fill="#f2e9e6" text-anchor="middle" letter-spacing="6">CABINETS &amp; DESIGN</text>
  <text class="sans" x="600" y="445" font-size="50" fill="var(--ink)" text-anchor="middle" letter-spacing="4">(504) 555-0187</text>
  <rect class="accent" x="375" y="470" width="465" height="38" rx="8"/>
  <text class="sans" x="607" y="498" font-size="28" fill="#f2e9e6" text-anchor="middle" letter-spacing="5">@verdellcabinets</text>
  <rect class="accent" x="232" y="490" width="40" height="200" rx="8"/>
  <rect class="accent" x="928" y="490" width="40" height="200" rx="8"/>
  <rect x="222" y="715" width="756" height="70" fill="var(--maroon-deep)"/>
  <text class="sans" x="600" y="759" font-size="22" fill="#fff" text-anchor="middle" letter-spacing="5">www.verdellcabinets.example</text>
  <path class="trim" d="M210,785 L990,785 L1000,880 L980,990 L220,990 L200,880 Z"/>
  <rect class="tyre" x="255" y="960" width="90" height="55" rx="10"/>
  <rect class="tyre" x="855" y="960" width="90" height="55" rx="10"/>
</svg>

</body>
</html>
```